Company or website name
- Jardin Lumineux
- Slogan or Tagline
- No Taglines, but each description listed here needs to be on the front label of each of these wines.
- Describe your company and organization and target audience
- Consumers buying wine aged 30+, restaurants. Of wine buyers, 55% are female shopping at major grocery chains.
- The design should have the following
- The style should marry traditional sophistication with a touch of contemporary fun. It should tell knowledgeable wine buyers that it is a serious, quality product, but have enough light to attract the novice wine buyers and impulse buyers. Must have: 1) Jardin Lumineux (brand name) 2) Method Traditionelle 3) Appellation Cremant de Limoux Controlee 4) Product of France -Brut -Brut RoseFountaine de la Vie means "Bright Garden" in French We would like this idea implemented into the design of the label. As a sparkling wine, bubbles are what spring from this fountain.
- This design should not have this in the entries
- No use of Gold or Gold Foil (scratches too easily). Also, black labels tend to scuff and don't travel well (plus they don't stand out on the shelves as much). Not too frilly – this is a quality product. We do not want to turn off serious wine buyers because they don’t take the label seriously.

```html
<!DOCTYPE html>
<html lang="en">
<head>
<meta charset="utf-8">
<title>Jardin Lumineux – Crémant de Limoux Label</title>
<link rel="stylesheet" href="https://fonts.googleapis.com/css2?family=Cormorant+Garamond:wght@500;600&display=swap">
<style>
  :root {
    --backdrop-light: #f4f4f4;
    --backdrop-dark: #cfcfcf;
    --label-cream: #fdf8dc;
    --label-border: #5c0d12;
    --ink-maroon: #5a1418;
    --ornament-peach: #f6c99a;
  }
  * { margin: 0; padding: 0; box-sizing: border-box; }
  html, body {
    width: 1200px;
    height: 880px;
    overflow: hidden;
  }
  body {
    background: radial-gradient(ellipse at 50% 35%, var(--backdrop-light) 0%, #e2e2e2 55%, var(--backdrop-dark) 100%);
    font-family: "Cormorant Garamond", Georgia, serif;
    color: var(--ink-maroon);
    position: relative;
  }
  .wine-label {
    position: absolute;
    left: 330px;
    top: 90px;
    width: 540px;
    height: 700px;
  }
  .wine-label__shape {
    position: absolute;
    inset: 0;
  }
  .wine-label__text {
    position: absolute;
    inset: 0;
    text-align: center;
  }
  .wine-label__line {
    position: absolute;
    left: 0;
    right: 0;
    letter-spacing: 0.04em;
    font-weight: 500;
  }
  .origin { top: 70px; font-size: 17px; }
  .appellation { top: 163px; font-size: 24px; }
  .brand-name {
    top: 250px;
    font-size: 62px;
    font-weight: 600;
    line-height: 1.05;
    letter-spacing: 0.02em;
  }
  .method { top: 476px; font-size: 22px; line-height: 1.15; letter-spacing: 0.06em; }
  .cuvee { top: 578px; font-size: 30px; font-weight: 600; letter-spacing: 0.06em; }
</style>
</head>
<body>
  <main class="wine-label" aria-label="Jardin Lumineux Brut Rosé front label">
    <svg class="wine-label__shape" width="540" height="700" viewBox="0 0 540 700" aria-hidden="false">
      <defs>
        <radialGradient id="ornament-glow" cx="50%" cy="50%" r="50%">
          <stop offset="0%" stop-color="var(--ornament-peach)" stop-opacity="0.55"/>
          <stop offset="100%" stop-color="var(--ornament-peach)" stop-opacity="0"/>
        </radialGradient>
        <clipPath id="label-oval">
          <ellipse cx="270" cy="350" rx="262" ry="342"/>
        </clipPath>
      </defs>
      <ellipse cx="270" cy="350" rx="266" ry="346" fill="var(--label-cream)" stroke="var(--label-border)" stroke-width="8"/>
      <g clip-path="url(#label-oval)">
        <ellipse role="img" aria-label="Peach flourish ornament, top left" cx="110" cy="110" rx="110" ry="90" fill="url(#ornament-glow)"/>
        <ellipse role="img" aria-label="Peach flourish ornament, top right" cx="430" cy="110" rx="110" ry="90" fill="url(#ornament-glow)"/>
        <ellipse role="img" aria-label="Peach floral motif, top centre" cx="270" cy="30" rx="34" ry="26" fill="url(#ornament-glow)"/>
        <ellipse role="img" aria-label="Peach flourish ornament, bottom left" cx="110" cy="590" rx="110" ry="90" fill="url(#ornament-glow)"/>
        <ellipse role="img" aria-label="Peach flourish ornament, bottom right" cx="430" cy="590" rx="110" ry="90" fill="url(#ornament-glow)"/>
        <ellipse role="img" aria-label="Peach floral motif, bottom centre" cx="270" cy="670" rx="34" ry="26" fill="url(#ornament-glow)"/>
      </g>
    </svg>
    <div class="wine-label__text">
      <p class="wine-label__line origin">PRODUCT OF FRANCE</p>
      <p class="wine-label__line appellation">CREMANT DE LIMOUX</p>
      <h1 class="wine-label__line brand-name">Jardin<br>Lumineux</h1>
      <p class="wine-label__line method">METHOD<br>TRADITIONELLE</p>
      <p class="wine-label__line cuvee">BRUT ROSÉ</p>
    </div>
  </main>
</body>
</html>
```